依頼概要
■依頼の目的/概要
「ひなげし名品の会」は足利市内の26の店舗がそれぞれの良い所を伸ばそうとする「逸品運動」を中心に共同で事業を行う組織です。
栃木県足利市は国宝霞峰寺、日本遺産千草学舎などの重要な史跡が点在すところから東の京都、北の鎌倉などと言われることがあります。また、霧見川橋、スカイプラザ、森下はるおの故郷など観光などのポイントが多数あります。
※添付ファイルに会員のカタログがあります。

■依頼詳細
「ひなげし名品の会」加盟の店舗は市内の各所に点在しております。そのためそれぞれの店舗の店頭に飾れるような「のぼり旗」のデザインを募集します。
※添付ファイルに地図があります。

■重視する点
【必須項目】
「ひなげし名品の会」という文字表記

のぼり旗という制約のあるデザインの中で名品会らしさ、足利らしさなどを取り込んだものを希望します。通常ののぼり旗の概念を逸脱するものでも結構ですが、予算が必要以上にかかり様なアイデアは採用が難しくなる可能性がございます。

その他何かご不明な点がございましたら、お気軽にご質問下さい。
よろしくお願いいたします。
足利市のイメージキャラクターをのぼりデザインに使用する事は可能です。
ただし「ひなげし名品会」のイメージキャラクターではございませんのでご確認ください。
なお、キャラクター使用許諾につきましては当会にて行います。
添付データとして「まさとき君」のイラストレータデータを添付させていただきますのでこちらを使用願います。
(※当依頼以外でまさとき君の画像当を使用する場合は霜月観光協会の許可が必要ですのでご注意ください。)
名品の会全体会議にてデザインの選定を行う予定です。
そのため直前の3月14日まで受付を延長させていただきます。
より多くの提案をお願いしたいと思います。
■ 選んだ理由

名品の会の会員からのアンケート調査に基づいて決定いたしました。

■ 提案者全員のお礼・コメント

このたびは名品会ののぼりをデザイン頂き誠にありがとうございます。
市内の各所にこのデザインが掲載されお客様に親しまれるように頑張りたいと思います。

```html
<!DOCTYPE html>
<html lang="ja">
<head>
<meta charset="utf-8">
<title>ひなげし名品の会 のぼり旗</title>
<link rel="stylesheet" href="https://fonts.googleapis.com/css2?family=Yuji+Boku&family=Yuji+Syuku&display=swap">
<style>
  :root {
    --banner-bg: #6c2337;
    --banner-bg-deep: #5f1d30;
    --lettering: #c7b4bb;
    --leaf-red: #8a2a2c;
    --leaf-gold: #b98a4e;
  }
  html, body {
    margin: 0;
    padding: 0;
    width: 1200px;
    height: 3584px;
    overflow: hidden;
    background: var(--banner-bg);
  }
  .banner {
    position: relative;
    width: 1200px;
    height: 3584px;
    background: linear-gradient(180deg, var(--banner-bg) 0%, var(--banner-bg-deep) 100%);
    overflow: hidden;
  }
  .banner-text {
    position: absolute;
    margin: 0;
    color: var(--lettering);
    writing-mode: vertical-rl;
    line-height: 1;
  }
  .banner-prefix {
    left: 850px;
    top: 230px;
    font-family: "Yuji Syuku", serif;
    font-size: 140px;
    letter-spacing: 10px;
  }
  .banner-title {
    left: 280px;
    top: 820px;
    font-family: "Yuji Boku", serif;
    font-size: 640px;
    font-weight: 400;
    letter-spacing: 120px;
  }
  .banner-suffix {
    font-family: "Yuji Syuku", serif;
    font-size: 190px;
  }
  .banner-suffix--no { left: 900px; top: 2560px; }
  .banner-suffix--kai { left: 270px; top: 2850px; }
  .maple-branch {
    position: absolute;
    left: 560px;
    top: 2800px;
    width: 600px;
    height: 760px;
    background: radial-gradient(ellipse at 45% 45%, var(--leaf-red) 0%, var(--leaf-gold) 55%, rgba(185,138,78,0) 75%);
    opacity: 0.75;
  }
</style>
</head>
<body>
  <main class="banner">
    <p class="banner-text banner-prefix">ひなげし</p>
    <h1 class="banner-text banner-title">名品</h1>
    <span class="banner-text banner-suffix banner-suffix--no">の</span>
    <span class="banner-text banner-suffix banner-suffix--kai">会</span>
    <div class="maple-branch" role="img" aria-label="紅葉した楓の枝のイラスト"></div>
  </main>
</body>
</html>
```